Executive retreat/workshop flyer for Keystone Passage

Our company, Keystone Passage, runs intensive week long residential retreats for executives suffering from burnout syndrome. We have a programme of therapy which will enable clients to get clarity on what they want out of life and how to achieve it.

Our website is www.keystonepassage.example. The flyer should have a consistent look and feel to the website. The flyer should be suitable for electronic distribution as well as printing.

The copy should read:

What is it all for? (IN BIG BOLD FONT)

We invite you to The Keystone Passage

Discover a more meaningful way of being in this world and put passion and purpose back into your life.

Our leading experts will guide you through a holistic program of intellectual, physical, emotional, spiritual and financial work.

You will:

- Draw up a vision of how you want to live your life
- Understand negative behavior loops and how to manage them
- Rebalance relationships which have suffered from stress and neglect
- Examine your attitudes towards money through the Octavial System
- Access practical advice on how to implement your goals

Please join us in the beautiful Tarrowby Peninsula this August for a life-changing journey.

This is an intensive program custom tailored to your individual needs. We can only take on a very limited number of participants to maintain intimacy and quality of attention. Book early to avoid disappointment.

Details:

date - mon 27 August - sat 1 sept 2012

Venue- kestrelwood Eco retreat, stony vale, Australia, 1 hour from Melbourne

Price- Special launch offer of US$ 13,860 which is a 30% discount off the normal price of US$ 19,800

10% of profits go to charity

All accommodation, food and individual consultations included.

Please email info@keystonepassage.example or contact Marnie at 9316 2047

Target Market(s)

Senior executives and leaders mostly with a financial background.

Industry/Entity Type

Residential

Requirements
Must have
• The brochure should look clear in electronic and print format. Can use photos which I've attached.
Nice to have
• Should have a warm, serene feel but appear professional and reliable.

```html
<!DOCTYPE html>
<html lang="en">
<head>
<meta charset="utf-8">
<title>The Keystone Passage – Retreat Flyer</title>
<link href="https://fonts.googleapis.com/css2?family=Source+Sans+3:ital,wght@0,400;0,600;0,700;1,400;1,700&family=Cinzel:wght@400&display=swap" rel="stylesheet">
<style>
:root{
  --stage:#671f61;
  --paper:#ffffff;
  --olive:#7d7b22;
  --olive-light:#8d8a2a;
  --plum:#5e1a5e;
  --ink:#4a4a4a;
  --ink-soft:#666;
  --mist:#e4e4e6;
  --lilac:#ece4ee;
}
*{margin:0;padding:0;box-sizing:border-box}
html,body{width:1200px;height:900px;overflow:hidden;background:var(--stage)}
body{font-family:"Source Sans 3",Arial,sans-serif;position:relative}
.flyer{position:absolute;left:315px;top:45px;width:583px;height:813px;background:var(--paper)}
.flyer > *{position:absolute}

.brand{left:40px;top:62px;font-family:"Cinzel",serif;font-size:15px;color:var(--olive);letter-spacing:.5px;display:flex;align-items:center;gap:8px}
.brand-dot{width:14px;height:14px;border-radius:50%;background:var(--plum)}

.hero{left:37px;top:93px;width:512px;height:220px;overflow:hidden}
.hero-photo{position:absolute;inset:0;background:linear-gradient(180deg,#fdf7ea 0%,#fbe9d2 40%,#f4b59a 65%,#e65a3c 80%,#f1c9b8 100%)}
.hero-title{position:absolute;right:20px;top:22px;font-size:37px;font-weight:700;font-style:italic;color:var(--olive);line-height:44px}
.hero-band{position:absolute;left:0;right:0;bottom:0;height:56px;background:rgba(255,255,255,.72)}
.hero-invite{position:absolute;right:16px;bottom:16px;font-size:17px;font-weight:700;font-style:italic;color:var(--olive)}

.accent{left:37px;top:333px;width:124px;height:76px;border-radius:60% 10% 60% 10%;background:var(--lilac)}
.intro{left:174px;top:327px;width:378px;color:var(--plum)}
.intro-lead{font-size:14.5px;font-weight:700;line-height:18px}
.intro-lead span{display:block;font-weight:400;font-size:17px}
.intro-body{margin-top:10px;font-size:12.3px;font-weight:700;line-height:15px;letter-spacing:-.1px}

.section-bar{left:37px;width:511px;height:20px;background:var(--olive);color:#fff;font-size:14px;font-weight:400;padding-left:12px;line-height:20px}
.bar-will{top:425px}
.bar-details{top:619px}

.benefits{left:50px;top:453px;list-style:none;font-size:12.5px;color:var(--ink);line-height:18px}
.benefits li,.details li{display:flex;align-items:center;gap:14px}
.leaf{width:18px;height:8px;border-radius:50%;background:var(--olive);flex:none}

.invite-line{left:37px;top:550px;font-size:13.3px;color:var(--olive)}
.fine{left:37px;top:576px;width:513px;font-size:10px;line-height:11.5px;color:var(--ink-soft)}

.details{left:50px;top:651px;list-style:none;font-size:11px;line-height:13px;color:var(--ink)}
.details li{align-items:flex-start;margin-bottom:8px}
.details .leaf{margin-top:2px}
.label{color:var(--olive)}
.figure{font-size:14px;color:var(--olive-light);line-height:13px}
.charity{left:79px;top:725px;font-size:15px;line-height:18px;color:var(--olive-light)}

.footer-box{left:37px;top:754px;width:511px;height:36px;background:var(--mist);padding:4px 0 0 43px;font-size:11px;font-style:italic;color:var(--ink-soft);line-height:13.5px}
.footer-box a{color:var(--olive);text-decoration:none}
</style>
</head>
<body>
<main class="flyer">
  <div class="brand"><span class="brand-dot"></span>The Keystone Passage</div>

  <section class="hero">
    <div class="hero-photo" role="img" aria-label="Red poppies in a soft sunlit meadow"></div>
    <h1 class="hero-title">What is it all for?</h1>
    <div class="hero-band"></div>
    <p class="hero-invite">We invite you to The Keystone Passage</p>
  </section>

  <div class="accent" role="img" aria-label="Faint leaf decoration"></div>
  <div class="intro">
    <p class="intro-lead">Discover a more meaningful way of being in this world <span>and put passion and purpose back into your life.</span></p>
    <p class="intro-body">Our leading experts will guide you through a holistic program of intellectual, physical, emotional, spiritual and financial work.</p>
  </div>

  <h2 class="section-bar bar-will">YOU WILL:</h2>
  <ul class="benefits">
    <li><span class="leaf"></span>Draw up a vision of how you want to live your life</li>
    <li><span class="leaf"></span>Understand negative behavior loops and how to manage them</li>
    <li><span class="leaf"></span>Rebalance relationships which have suffered from stress and neglect</li>
    <li><span class="leaf"></span>Examine your attitudes towards money through the Octavial System</li>
    <li><span class="leaf"></span>Access practical advice on how to implement your goals</li>
  </ul>

  <p class="invite-line">Please join us in the beautiful Tarrowby Peninsula this August for a life-changing journey.</p>
  <p class="fine">This is an intensive program custom tailored to your individual needs. We can only take on a very limited number of participants to maintain intimacy and quality of attention. Book early to avoid disappointment.</p>

  <h2 class="section-bar bar-details">DETAILS:</h2>
  <ul class="details">
    <li><span class="leaf"></span><span><span class="label">DATE:</span> mon 27 August - sat 1 sept 2012</span></li>
    <li><span class="leaf"></span><span><span class="label">VENUE:</span> kestrelwood Eco retreat, stony vale, Australia, 1 hour from Melbourne</span></li>
    <li><span class="leaf"></span><span><span class="label">PRICE:</span> special launch offer of US$ <span class="figure">13,860</span> which is a <span class="figure">30%</span> discount<br>off the normal price of US$ 19,800</span></li>
  </ul>
  <p class="charity">10% of profits go to charity</p>

  <div class="footer-box">
    All accommodation, food and individual consultations included.<br>
    Please email <a href="mailto:info@keystonepassage.example">info@keystonepassage.example</a> or contact <a>Marnie at 9316 2047</a>
  </div>
</main>
</body>
</html>
```